ReDesign Website for a more Bold approach

Hello! I'd like to redesign my website: holvencrest.com

I'd like to add one thing that's not on my website which is a blog. The design around the blog should be put time into as I will be putting out incredibly great content and want it to attract viewers.

I get a lot of inspiration from ruvtal.com (the way they flow the big statements across each screen, colors)
moorlane.vc (the simplicity behind the design is beautiful)

I like modern very simple but bold approaches.

I am going to attach my logo here and if it can be thought of when making the design of the website. Thanks!

Industry/Entity Type

Finance and Private Equity

Number of Pages Required

3 page

Font styles to use
Serif
Sans Serif

Colors
0054AA
0677BA
7BADD7
CADEEF
E8F1F8
0094D4
00A9DD
6FCCEA
C7EBF8
E9F6FB
00AB8E
00BBA5
67D7C9
C6EFE9
E9F9F6

Requirements
Must have
• My project must have a Home, Expertise, Story, Clients, Approach, Blog, Contact
Nice to have
• It would be nice to have these tabs reduced to 1-3 pages
Should not have
• My project must not have bright colors.

```html
<!DOCTYPE html>
<html lang="en">
<head>
<meta charset="utf-8">
<title>Holvencrest Ventures</title>
<link href="https://fonts.googleapis.com/css2?family=Montserrat:wght@400;500;600;700&family=Lato:wght@400;700&display=swap" rel="stylesheet">
<style>
:root{
  --navy:#0d1b36;
  --royal:#0a2a82;
  --blue:#1a56b0;
  --blue-deep:#123f8c;
  --card:#dde7f3;
  --ink:#1b1b1b;
  --body:#333;
  --grey-band:#efefef;
  --footer:#e6e6e6;
  --logo-grey:#8a8a8a;
  --white:#fff;
}
*{margin:0;padding:0;box-sizing:border-box}
html,body{width:1200px;height:4441px;overflow:hidden;background:var(--white)}
body{font-family:'Lato',sans-serif;color:var(--body);position:relative}
.heading{font-family:'Montserrat',sans-serif;font-weight:500;color:var(--ink)}
section,header,footer{position:absolute;left:0;width:1200px}
.abs{position:absolute}
.btn{position:absolute;background:var(--royal);color:var(--white);font-family:'Montserrat',sans-serif;font-weight:600;font-size:15px;display:flex;align-items:center;justify-content:center;letter-spacing:.3px}

/* nav */
.site-nav{top:0;height:74px;background:var(--navy)}
.brand{left:110px;top:22px;font-family:'Montserrat',sans-serif;font-weight:700;font-size:23px;color:var(--white);letter-spacing:.5px}
.nav-links{right:111px;top:28px;display:flex;gap:0;font-family:'Montserrat',sans-serif;font-size:13.5px;color:var(--white);list-style:none}
.nav-links li{margin-left:44px}

/* hero */
.hero{top:74px;height:559px;background:linear-gradient(135deg,#3a2a20 0%,#5b4535 35%,#7a6a5e 60%,#4a3b30 100%)}
.hero-shade{inset:0;background:rgba(20,15,12,.35)}
.hero-title{left:0;width:1200px;top:190px;text-align:center;font-family:'Montserrat',sans-serif;font-weight:500;font-size:46px;line-height:57px;color:var(--white)}
.hero-chevron{left:578px;top:325px}

/* expertise */
.expertise{top:633px;height:675px}
.section-title{left:0;width:1200px;text-align:center;font-size:37px}
.title-rule{left:555px;height:5px;width:90px;background:var(--royal)}
.exp-card{top:144px;width:311px;height:378px;background:var(--card)}
.exp-card .photo{left:0;top:0;width:311px;height:237px}
.exp-card h3{position:absolute;left:22px;top:262px;font-family:'Montserrat',sans-serif;font-weight:500;font-size:19px;color:var(--ink)}
.exp-card p{position:absolute;left:22px;top:300px;width:270px;font-size:13.5px;line-height:26px;color:var(--ink)}

/* story */
.story{top:1308px;height:611px}
.story h2,.approach h2{font-size:37px;position:absolute}
.story .text,.approach .text{position:absolute;font-size:14.2px;line-height:25.8px;color:var(--ink)}

/* stats */
.stats{top:1919px;height:233px;background:linear-gradient(120deg,var(--blue-deep),var(--blue) 45%,#1d5fbd)}
.stat{top:0;width:244px;height:233px;text-align:center;color:var(--white)}
.stat .num{position:absolute;top:65px;width:100%;font-family:'Montserrat',sans-serif;font-weight:500;font-size:42px}
.stat .label{position:absolute;top:133px;width:100%;font-family:'Montserrat',sans-serif;font-weight:500;font-size:19px;line-height:25px}
.divider{top:60px;width:2px;height:112px;background:var(--white)}

/* approach */
.approach{top:2152px;height:619px}

/* blog */
.blog{top:2771px;height:654px}
.blog h2{font-weight:600}
.blog-card{top:144px;width:430px;height:419px}
.blog-feature{background:linear-gradient(135deg,#1a4fa4,#1f5fb8);color:var(--white);text-align:center}
.blog-feature h3{position:absolute;top:128px;width:100%;font-family:'Montserrat',sans-serif;font-weight:500;font-size:22px}
.blog-feature .rule{left:191px;top:164px;width:48px;height:2px;background:var(--white)}
.blog-feature p{position:absolute;top:178px;left:50px;width:330px;font-size:14px;line-height:26px}
.blog-feature .more{position:absolute;top:268px;width:100%;font-family:'Montserrat',sans-serif;font-weight:600;font-size:14px;display:flex;justify-content:center;align-items:center;gap:8px}

/* portfolio */
.portfolio{top:3425px;height:249px;background:var(--grey-band)}
.client{top:140px;width:200px;text-align:center;font-family:'Montserrat',sans-serif;font-weight:600;font-size:38px;color:var(--logo-grey)}

/* contact */
.contact{top:3674px;height:690px}
.col-title{font-family:'Montserrat',sans-serif;font-weight:500;font-size:21px;color:var(--ink)}
.field-label{font-size:13.5px;color:var(--ink)}
.field{width:396px;height:36px;border:1px solid #555;background:var(--white)}
.info{font-size:14px;line-height:26px;color:var(--ink);width:370px}

.site-footer{top:4364px;height:77px;background:var(--footer);display:flex;align-items:center;justify-content:center;font-size:14px;color:var(--ink)}
</style>
</head>
<body>

<header class="site-nav">
  <div class="abs brand">HOLVENCREST VENTURES</div>
  <ul class="abs nav-links">
    <li>HOME</li><li>EXPERTISE</li><li>STORY</li><li>CLIENTS</li><li>APPROACH</li><li>CONTACT</li>
  </ul>
</header>

<section class="hero" role="img" aria-label="Desk scene with business partners shaking hands over documents and a laptop">
  <div class="abs hero-shade"></div>
  <h1 class="abs hero-title">BUILT BY FOUNDERS FOR<br>FOUNDERS</h1>
  <svg class="abs hero-chevron" width="44" height="26" viewBox="0 0 44 26"><polyline points="3,3 22,22 41,3" fill="none" stroke="#fff" stroke-width="5"/></svg>
</section>

<section class="expertise">
  <h2 class="abs heading section-title" style="top:50px">AREA OF EXPERTISE</h2>
  <div class="abs title-rule" style="top:98px"></div>

  <article class="abs exp-card" style="left:110px">
    <div class="abs photo" role="img" aria-label="Team gathered around a table in a dark office" style="background:linear-gradient(160deg,#1e2b3c,#3d4d60 60%,#263242)"></div>
    <h3>NETWORK SUPPORT</h3>
    <p>Help you build your network, introducing you to the right people in the right places.</p>
  </article>
  <article class="abs exp-card" style="left:445px">
    <div class="abs photo" role="img" aria-label="Cheerful team giving thumbs up in an office" style="top:-5px;left:5px;width:306px;background:linear-gradient(160deg,#5d6670,#8d96a0 50%,#4b5560)"></div>
    <h3>MARKETING</h3>
    <p>Consult on marketing process, strategies and implementation across your startup.</p>
  </article>
  <article class="abs exp-card" style="left:778px">
    <div class="abs photo" role="img" aria-label="Colleagues in a meeting room around a laptop" style="background:linear-gradient(160deg,#8a8c8f,#b9bbbd 50%,#55595e)"></div>
    <h3>RAISING CAPITAL</h3>
    <p>Reach out to our extensive connections to raise vital capital for your startup.</p>
  </article>

  <div class="btn" style="left:529px;top:555px;width:140px;height:48px">VIEW ALL</div>
</section>

<section class="story">
  <h2 class="heading" style="left:110px;top:53px">OUR STORY</h2>
  <p class="text" style="left:110px;top:113px;width:478px">Holvencrest Ventures is a venture capital studio firm based in Austin TX with a laser focus on raising solid capital for startups and helping businesses jumpstart their revenue. Founded in 2020 by investment expert Marcus Delane, Holvencrest Ventures combines proven experience in the venture capital field with a data-driven business analysis strategy to secure capital and reinforce revenue streams for startups and established businesses. Born from the idea that the best way to help founders thrive is to understand their strengths, their weaknesses, their ambitions and their needs - our specialists have been through the entire startup process themselves, and that experience forms our unique approach to business support. Marcus's work in the sector has seen him take on the biggest and the best, working with iconic business figures to leave an indelible mark on the U.S. startup scene.</p>
  <div class="btn" style="left:110px;top:504px;width:245px;height:46px">LET'S WORK TOGETHER &gt;</div>
  <div class="abs" role="img" aria-label="Smiling businesswoman seated at a meeting table with colleagues behind her" style="left:638px;top:0;width:562px;height:611px;background:linear-gradient(150deg,#7c8794,#b8bfc7 45%,#d9dadb 70%,#6f7782)"></div>
</section>

<section class="stats">
  <div class="abs stat" style="left:111px"><div class="num">$40M+</div><div class="label">MONEY RAISED</div></div>
  <div class="abs divider" style="left:351px"></div>
  <div class="abs stat" style="left:354px"><div class="num">$125M+</div><div class="label">ATTRIBUTE<br>REVENUE</div></div>
  <div class="abs divider" style="left:597px"></div>
  <div class="abs stat" style="left:597px"><div class="num">11</div><div class="label">COMPANY EXITS</div></div>
  <div class="abs divider" style="left:842px"></div>
  <div class="abs stat" style="left:842px"><div class="num">2</div><div class="label">AWARDS WON</div></div>
</section>

<section class="approach">
  <div class="abs" role="img" aria-label="Businessman holding a notebook talking with a colleague in a glass office" style="left:0;top:0;width:559px;height:619px;background:linear-gradient(150deg,#46525e,#7d8894 45%,#a9a39a 70%,#3f4a55)"></div>
  <h2 class="heading" style="left:609px;top:55px">OUR APPROACH</h2>
  <p class="text" style="left:609px;top:119px;width:478px">We've built our approach to helping your startup thrive based around three key developmental pillars that guarantee results for our partners. First pillar is expertise. We've built our firm on a bank of insights, knowledge and proficiencies honed over years of working with the biggest names in venture capitalism – that experience forms the backbone of every project, every pitch and every investment. Second pillar is collaboration. We believe that the best partnerships start with a combined and cooperative approach that benefits all parties every step of the way. We'll always keep our partners up-to-date with our work using regular touchpoints and reports. Third and final pillar is trust. We know that our clients and our partners know their industry better than we do, so we trust their input and their ideas – pairing them up with our own business intelligence to guarantee success.</p>
  <div class="btn" style="left:610px;top:508px;width:243px;height:48px">LET'S WORK TOGETHER &gt;</div>
</section>

<section class="blog">
  <h2 class="abs heading section-title" style="top:62px;font-size:35px">Our Blog</h2>
  <div class="abs blog-card" role="img" aria-label="Smiling businesswoman standing in an office corridor" style="left:153px;background:linear-gradient(150deg,#3b4a58,#9aa3ab 45%,#d6d6d2 60%,#4c5866)"></div>
  <article class="abs blog-card blog-feature" style="left:615px">
    <h3>Lorem Ipsum</h3>
    <div class="abs rule"></div>
    <p>Lorem ipsum dolor sit amet, consectetur adipiscing elit, sed do eiusmod tempor incididunt ut labore et dolore magna aliqua.</p>
    <div class="more">Learn More
      <svg width="13" height="13" viewBox="0 0 13 13"><circle cx="6.5" cy="6.5" r="6.5" fill="#fff"/><polyline points="5,3.5 8,6.5 5,9.5" fill="none" stroke="#1a4fa4" stroke-width="1.8"/></svg>
    </div>
  </article>
</section>

<section class="portfolio">
  <h2 class="abs heading section-title" style="top:52px;font-size:35px">PORTFOLIO</h2>
  <div class="abs client" style="left:110px">Quarro</div>
  <div class="abs client" style="left:357px;font-weight:400">Tressly</div>
  <div class="abs client" style="left:607px">Orbana</div>
  <div class="abs client" style="left:874px">Fundlet</div>
</section>

<section class="contact">
  <h2 class="abs heading section-title" style="top:66px;font-size:35px">BUILD WITH US</h2>

  <div class="abs col-title" style="left:178px;top:170px">Contact Us</div>
  <div class="abs field-label" style="left:178px;top:218px">First Name</div>
  <div class="abs field" style="left:178px;top:239px"></div>
  <div class="abs field-label" style="left:178px;top:295px">Email</div>
  <div class="abs field" style="left:178px;top:315px"></div>
  <div class="abs field-label" style="left:178px;top:373px">Phone</div>
  <div class="abs field" style="left:178px;top:393px"></div>
  <div class="abs field-label" style="left:178px;top:443px">Message</div>
  <div class="abs field" style="left:178px;top:465px;height:112px"></div>
  <div class="btn" style="left:471px;top:603px;width:101px;height:38px;font-size:14px">Submit</div>

  <div class="abs col-title" style="left:653px;top:169px">Head Office</div>
  <p class="abs info" style="left:653px;top:213px">Lorem ipsum dolor sit amet, consectetur adipiscing elit, sed do eiusmod tempor incididunt ut labore et dolore magna aliqua.</p>
  <p class="abs info" style="left:655px;top:313px">info@holvencrest.com<br>Tel: +1 888 888 8888</p>
  <div class="abs col-title" style="left:653px;top:402px">Employment</div>
  <p class="abs info" style="left:653px;top:445px">Lorem ipsum dolor sit amet, consectetur adipiscing elit, sed do eiusmod tempor incididunt ut labore et dolore magna aliqua.</p>
  <div class="abs col-title" style="left:653px;top:549px;font-weight:600">Get a quote: +1 888 888 8888</div>
</section>

<footer class="site-footer">COPYRIGHT © 2022 HOLVENCREST.COM</footer>

</body>
</html>
```